Norvell Property Services LLC. Commercial & Residential

PROFESSIONAL WINDOW WASHING! professional dryer vent cleaning (prevent fires, $aves money, Lowers your electric bill, save your dryer, less drying time, ask how!)gutter clean outs and tune-up *Lowest Price Quotes Guaranteed!Straightforward Consultancy and Advice to empower homeowners and find solutions that fit your budget!non pressure house cleaning "no pressure...No Damage!Interior & Exterior House Painting call for free in-home consultationPre & Post Tenant Clean-Up PaintGenerator Maintenance Comprehensive Landlord Services & REO (special requests considered) no job too small)!

I would like my business cards to be as professional as possible. I provide property services to commercial and residential clients and need these cards to draw attention and catch ones eye. I have never had business cards for this the services I provide. And I need them so that business owners will trust that our services are the best and also homeowners will call based on the information they see on these cards., I want the window washing service to be the main focal point because it the main service provided. thank you Added Saturday, July 4, 2015

Target Market(s)

Property Services and professional window cleaning highlighted on the front of card rounded edges for card and sleek eye catching cards thank you

Industry/Entity Type

Property Maintenance

Contact Information for Business Card

518-555-0147 Direct. norvellpropertyservicesllc@brindlemail.net

Requirements
Must have
• Professional appearance and eye catch design Property Services as a general point with professional window washing as a highlighted service and all the rest of the services on back of card
Nice to have
• vivid colors but professional appearance

```html
<!DOCTYPE html>
<html lang="en">
<head>
<meta charset="utf-8">
<title>Norvell Property Services LLC – Business Card</title>
<link href="https://fonts.googleapis.com/css2?family=Lato:wght@400;700;900&display=swap" rel="stylesheet">
<style>
  :root {
    --backdrop: #2b2b2c;
    --card: #161718;
    --card-edge: #242526;
    --accent: #2fa3d6;
    --text: #f2f2f2;
    --muted: #cfd2d4;
    --rule: #5b5e61;
  }
  * { margin: 0; padding: 0; box-sizing: border-box; }
  html, body { width: 1200px; height: 900px; overflow: hidden; }
  body {
    background: var(--backdrop);
    font-family: "Lato", Arial, sans-serif;
    color: var(--text);
    position: relative;
  }
  .card {
    position: absolute;
    top: 300px;
    width: 540px;
    height: 310px;
    border-radius: 26px;
    background: var(--card);
    border: 1px solid var(--card-edge);
    box-shadow: 0 10px 30px rgba(0,0,0,.45);
  }
  .card--front { left: 45px; display: flex; }
  .card--back { left: 615px; display: flex; align-items: center; justify-content: center; }

  .brand {
    width: 230px;
    display: flex;
    flex-direction: column;
    justify-content: center;
    align-items: center;
    padding: 0 18px;
  }
  .brand__name {
    color: var(--accent);
    font-weight: 900;
    font-size: 24px;
    line-height: 1.1;
    text-align: center;
    text-transform: uppercase;
    letter-spacing: .5px;
  }
  .brand__tagline {
    margin-top: 10px;
    padding-top: 7px;
    border-top: 1px solid var(--rule);
    color: var(--accent);
    font-size: 13px;
    text-align: center;
    width: 100%;
  }
  .divider {
    width: 1px;
    background: var(--rule);
    margin: 60px 0;
  }
  .contact {
    flex: 1;
    padding: 60px 16px 0 20px;
  }
  .contact__name { font-size: 24px; font-weight: 400; }
  .contact__role { color: var(--accent); font-size: 15px; margin-bottom: 16px; }
  .contact__address, .contact__lines { font-size: 14px; color: var(--muted); line-height: 1.45; }
  .contact__lines { margin-top: 14px; font-size: 12.5px; }
  .contact__label { color: var(--accent); display: inline-block; width: 16px; }

  .services {
    list-style: none;
    text-align: center;
    text-transform: uppercase;
    font-size: 14px;
    line-height: 1.6;
    color: var(--accent);
  }
  .services__headline { color: var(--text); font-weight: 700; }
  .services__gap { margin-top: 12px; }
</style>
</head>
<body>
  <section class="card card--front" aria-label="Business card front">
    <div class="brand">
      <div class="brand__name">Norvell Property Services LLC</div>
      <div class="brand__tagline">Professional Window Cleaning</div>
    </div>
    <div class="divider"></div>
    <div class="contact">
      <h1 class="contact__name">Marcus Hale</h1>
      <p class="contact__role">Managing Director</p>
      <p class="contact__address">12345, Address Goes Here<br>Country Name, 123456.</p>
      <p class="contact__lines">
        <span class="contact__label">T:</span>518-555-0147<br>
        <span class="contact__label">E:</span>norvellpropertyservicesllc@brindlemail.net<br>
        <span class="contact__label">W:</span>www.norvellproperty.net
      </p>
    </div>
  </section>

  <section class="card card--back" aria-label="Business card back">
    <ul class="services">
      <li class="services__headline">Professional Window Washing</li>
      <li>Lowest Price Quotes Guaranteed!</li>
      <li>Straightforward Consultancy</li>
      <li>Non Pressure House Cleaning</li>
      <li>No Pressure...No Damage!</li>
      <li>Interior &amp; Exterior House Painting</li>
      <li>Call for Free In-Home Consultation</li>
      <li>Pre &amp; Post Tenant Clean-Up Paint</li>
      <li>Generator Maintenance</li>
      <li class="services__gap">Comprehensive Landlord Services &amp; REO</li>
    </ul>
  </section>
</body>
</html>
```